Fiscal Sponsorship Program Flyer

We are seeking a designer to create a 1-2 flyer that explains our fiscal sponsorship program. This flyer will be used to recruit new projects that might be interested in utilizing our fiscal sponsorship services. The pertinent information about our program can be found in the attached PDF. For users who cannot access the PDF, please try this link: https://files.plovarimedia.net/deck/7QtR2wzoLkVa9pXcJ4nEuYhsT3bGdMf8eKqW5rZxN1yo/view?mode=public

Target Market(s)

New charitable projects that do not yet have their own 501(c)(3) status, and are seeking a fiscal sponsor.

Industry/Entity Type

Nonprofit/Charity

Requirements
Must have
• The flyer must include the language and detail included on the attached PDF. The desire is to reformat this to be more appealing and easy to read.

```html
<!DOCTYPE html>
<html lang="en">
<head>
<meta charset="utf-8">
<title>Wellspring Foundation – Fiscal Sponsorship Program</title>
<link rel="stylesheet" href="https://fonts.googleapis.com/css2?family=Playfair+Display:wght@700;900&family=Raleway:wght@400;500;600;700;800&display=swap">
<style>
  :root {
    --mint: #b1e4de;
    --coral: #f25c5f;
    --ink: #141414;
    --text: #2b2b2b;
    --muted: #6d6d6d;
    --line: #d9d9d9;
    --paper: #ffffff;
    --backdrop: #f1f1f1;
  }
  * { box-sizing: border-box; margin: 0; padding: 0; }
  html, body { width: 890px; height: 1200px; overflow: hidden; background: var(--backdrop); }
  body { font-family: "Raleway", Arial, sans-serif; color: var(--text); position: relative; }

  .page {
    position: absolute; left: 215px; width: 665px; height: 860px;
    background: var(--paper); overflow: hidden;
    transform: scale(0.69); transform-origin: 0 0;
    box-shadow: 0 6px 18px rgba(0,0,0,0.18);
  }
  .page--front { top: 4px; }
  .page--back { top: 602px; }
  .abs { position: absolute; }

  .section-heading {
    font-family: "Playfair Display", Georgia, serif; font-weight: 700;
    font-size: 20px; color: var(--coral); line-height: 1.1;
    border-left: 3px solid var(--coral); padding-left: 10px;
  }

  /* front page */
  .masthead { position: absolute; left: 0; top: 0; width: 665px; height: 284px; background: var(--mint); padding: 30px 46px 0; }
  .masthead__title { font-family: "Playfair Display", Georgia, serif; font-weight: 900; font-size: 63px; line-height: 0.98; color: var(--ink); }
  .masthead__rule { width: 72px; height: 4px; background: var(--coral); margin: 12px 0 10px; }
  .masthead__subtitle { font-family: "Playfair Display", Georgia, serif; font-weight: 900; font-size: 40px; line-height: 1.0; color: var(--coral); }

  .mission { left: 46px; top: 310px; width: 575px; }
  .mission p { font-size: 10.5px; line-height: 1.3; margin-top: 9px; }

  .about { left: 44px; top: 450px; width: 300px; }
  .about__body { font-size: 9.3px; line-height: 1.38; margin-top: 14px; }
  .about__question { color: var(--coral); font-size: 12.5px; font-weight: 500; line-height: 1.35; margin-top: 26px; }
  .about__criteria-intro { font-size: 10.5px; line-height: 1.3; margin-top: 16px; }
  .criteria { list-style: none; margin-top: 13px; }
  .criteria li { display: flex; gap: 9px; font-size: 10px; font-weight: 600; line-height: 1.3; margin-bottom: 5px; color: var(--ink); }
  .criteria__num { flex: 0 0 13px; height: 13px; border-radius: 50%; background: var(--coral); color: #fff; font-size: 8px; font-weight: 700; display: flex; align-items: center; justify-content: center; margin-top: 1px; }

  .philosophy { left: 375px; top: 440px; width: 241px; height: 338px; background: var(--coral); border-radius: 0 22px 0 22px; padding: 20px 16px 0 20px; color: #fff; }
  .philosophy__heading { font-family: "Playfair Display", Georgia, serif; font-weight: 700; font-size: 19.5px; line-height: 1.2; border-left: 3px solid #fff; padding-left: 9px; color: var(--ink); }
  .philosophy__heading .lead { color: #fff; }
  .philosophy p { font-size: 10.2px; font-weight: 600; line-height: 1.3; margin-top: 24px; }
  .philosophy p + p { margin-top: 14px; }

  .contact { position: absolute; left: 0; top: 812px; width: 665px; display: flex; justify-content: center; gap: 14px; font-size: 14px; font-weight: 500; color: var(--ink); }
  .contact__item { display: flex; align-items: center; gap: 7px; }
  .contact__item svg { width: 16px; height: 16px; }

  /* back page */
  .values { position: absolute; left: 0; top: 0; width: 665px; height: 258px; background: var(--coral); }
  .values__heading { position: absolute; left: 46px; top: 42px; font-family: "Playfair Display", Georgia, serif; font-weight: 700; font-size: 24px; color: #fff; border-left: 3px solid #fff; padding-left: 10px; line-height: 1.1; }
  .value { position: absolute; display: flex; gap: 12px; align-items: flex-start; }
  .value__icon { flex: 0 0 30px; height: 30px; border-radius: 50%; background: #fff; border: 2px solid #fff; box-shadow: 0 0 0 1.5px rgba(255,255,255,0.6); display: flex; align-items: center; justify-content: center; }
  .value__icon svg { width: 18px; height: 18px; }
  .value__title { font-size: 8px; font-weight: 800; color: var(--ink); text-transform: uppercase; line-height: 1.2; }
  .value__text { font-size: 8.4px; color: #fff; line-height: 1.3; }

  .commitments__heading { left: 46px; top: 280px; font-size: 23px; }
  .commit-list { position: absolute; list-style: none; top: 328px; }
  .commit-list li { display: flex; gap: 18px; font-size: 9.2px; font-weight: 600; line-height: 1.28; color: var(--ink); margin-bottom: 11px; }
  .commit-list svg { flex: 0 0 11px; width: 11px; height: 11px; margin-top: 1px; }
  .commit-list--left { left: 48px; width: 290px; }
  .commit-list--right { left: 359px; width: 262px; }
  .divider { position: absolute; left: 46px; top: 456px; width: 569px; height: 1px; background: var(--line); }
  .fees__heading { position: absolute; left: 0; top: 468px; width: 665px; text-align: center; font-family: "Playfair Display", Georgia, serif; font-weight: 700; font-size: 23px; color: var(--coral); }

  .fee-card { position: absolute; top: 513px; width: 178px; height: 282px; background: #fff; border: 1px solid #e4e4e4; border-radius: 10px; overflow: hidden; box-shadow: 0 3px 8px rgba(0,0,0,0.12); }
  .fee-card__head { height: 82px; background: var(--mint); clip-path: polygon(0 0, 100% 0, 100% 60%, 50% 100%, 0 60%); text-align: center; padding-top: 14px; font-size: 15px; font-weight: 800; line-height: 1.1; color: var(--ink); text-transform: uppercase; }
  .fee-card__body { padding: 8px 12px 0 16px; }
  .fee-card__label { font-size: 14.5px; font-weight: 800; color: var(--coral); text-transform: uppercase; margin-bottom: 6px; }
  .fee-card__note { font-size: 8.6px; color: var(--muted); line-height: 1.25; }
  .fee-card__sub { font-size: 8.6px; font-weight: 700; color: var(--ink); margin-bottom: 6px; }
  .fee-card ul { list-style: none; }
  .fee-card li { display: flex; gap: 7px; font-size: 8.8px; font-weight: 500; line-height: 1.25; color: var(--ink); margin-bottom: 6px; }
  .fee-card li svg { flex: 0 0 7px; width: 7px; height: 7px; margin-top: 2px; }
</style>
</head>
<body>
  <article class="page page--front">
    <header class="masthead">
      <h1 class="masthead__title">Wellspring<br>Foundation</h1>
      <div class="masthead__rule"></div>
      <h2 class="masthead__subtitle">Fiscal Sponsorship<br>Program</h2>
    </header>

    <section class="mission abs">
      <h3 class="section-heading">Mission &amp; Vision</h3>
      <p>The Wellspring Foundation, founded in 2010, exists to support social impact campaigns and organizations through educational, public engagement, and awareness efforts.</p>
      <p>Its vision is to strengthen the capacity of the social impact sector and its leaders by providing top-tier fiscal sponsorship services.</p>
    </section>

    <section class="about abs">
      <h3 class="section-heading">What is Fiscal Sponsorship?</h3>
      <p class="about__body">Fiscal sponsorship refers to the practice of non-profit organizations offering their legal and tax-exempt status to charitable projects or groups engaged in activities related to the sponsoring organization's mission. Fiscal sponsors provide oversight, financial management, and other administrative services to build the capacity of charitable projects.</p>
      <p class="about__question">What kinds of projects are eligible for fiscal sponsorship?</p>
      <p class="about__criteria-intro">Wellspring Foundation uses the following broad criteria to determine whether or not a project is eligible for fiscal sponsorship:</p>
      <ol class="criteria">
        <li><span class="criteria__num">1</span><span>Mission alignment with the Wellspring Foundation.</span></li>
        <li><span class="criteria__num">2</span><span>Whether or not the project provides an educational, social or charitable benefit.</span></li>
        <li><span class="criteria__num">3</span><span>Whether or not the project's activities follow the IRS regulations governing 501(c)(3) public charities.</span></li>
      </ol>
    </section>

    <aside class="philosophy abs">
      <h3 class="philosophy__heading"><span class="lead">Fiscal Sponsorship</span><br>Program<br>Philosophy</h3>
      <p>We believe we can accelerate the pace and scale of social change by providing strategic back office support to emerging projects, leaders and ideas.</p>
      <p>By providing light touch administrative and capacity building services, our fiscal sponsorship program takes the administrative burden off the shoulders of leaders and their projects to allow them to focus on what they do best achieving impact and changing the world.</p>
    </aside>

    <footer class="contact">
      <span class="contact__item"><svg viewBox="0 0 24 24" aria-hidden="true"><rect x="2" y="6" width="20" height="15" rx="1.5" fill="#f25c5f"/><path d="M2.5 7 L12 14.5 L21.5 7" fill="none" stroke="#fff" stroke-width="1.6"/></svg>info@wellspringcivic.org</span>
      <span class="contact__item"><svg viewBox="0 0 24 24" aria-hidden="true"><g fill="none" stroke="#f25c5f" stroke-width="1.8"><circle cx="12" cy="12" r="9.5"/><ellipse cx="12" cy="12" rx="4.2" ry="9.5"/><path d="M2.5 12h19M4 7h16M4 17h16"/></g></svg>wellspringcivic.org</span>
    </footer>
  </article>

  <article class="page page--back">
    <section class="values">
      <h3 class="values__heading">Organizational Values</h3>

      <div class="value" style="left:48px; top:84px; width:290px;">
        <span class="value__icon"><svg viewBox="0 0 24 24"><path d="M12 20s-7-4.5-7-9.5A3.8 3.8 0 0 1 12 8a3.8 3.8 0 0 1 7 2.5C19 15.5 12 20 12 20z" fill="#141414"/></svg></span>
        <div><p class="value__title">Trust:</p><p class="value__text">We believe that all successful partnerships begin with a foundation of trust.</p></div>
      </div>
      <div class="value" style="left:48px; top:132px; width:290px;">
        <span class="value__icon"><svg viewBox="0 0 24 24"><g fill="none" stroke="#141414" stroke-width="2.4"><circle cx="9" cy="12" r="5"/><circle cx="15" cy="12" r="5"/></g></svg></span>
        <div><p class="value__title">Relationships:</p><p class="value__text">Our partners are central to our work. We honor our relationships through respect, communication and transparency.</p></div>
      </div>
      <div class="value" style="left:48px; top:190px; width:290px;">
        <span class="value__icon"><svg viewBox="0 0 24 24"><g fill="#141414"><circle cx="12" cy="12" r="4.5"/><rect x="10.5" y="2" width="3" height="20"/><rect x="2" y="10.5" width="20" height="3"/><rect x="10.5" y="2" width="3" height="20" transform="rotate(45 12 12)"/><rect x="10.5" y="2" width="3" height="20" transform="rotate(-45 12 12)"/></g><circle cx="12" cy="12" r="2" fill="#fff"/></svg></span>
        <div><p class="value__title">Embrace Complexity and Risk:</p><p class="value__text">We understand that bold solutions to intractable social issues often require both complexity and risk.</p></div>
      </div>
      <div class="value" style="left:362px; top:84px; width:250px;">
        <span class="value__icon"><svg viewBox="0 0 24 24"><path d="M12 3a6 6 0 0 0-3.5 10.9V17h7v-3.1A6 6 0 0 0 12 3z" fill="#141414"/><rect x="9" y="18.3" width="6" height="2.2" fill="#141414"/></svg></span>
        <div><p class="value__title">Innovation:</p><p class="value__text">We embrace continuous improvement, bold creativity and change.</p></div>
      </div>
      <div class="value" style="left:362px; top:138px; width:250px;">
        <span class="value__icon"><svg viewBox="0 0 24 24"><path d="M12 20s-7-4.5-7-9.5A3.8 3.8 0 0 1 12 8a3.8 3.8 0 0 1 7 2.5C19 15.5 12 20 12 20z" fill="#141414"/><path d="M8 12h8" stroke="#fff" stroke-width="1.6"/></svg></span>
        <div><p class="value__title">Diversity:</p><p class="value__text">We believe that all voices matter and that effective solutions are created when decision-making is inclusive across social, cultural and economic backgrounds.</p></div>
      </div>
    </section>

    <h3 class="section-heading commitments__heading abs">Wellspring Foundation – Program Commitments</h3>
    <ul class="commit-list commit-list--left">
      <li><svg viewBox="0 0 12 12"><circle cx="6" cy="6" r="5" fill="none" stroke="#f25c5f" stroke-width="1"/><path d="M3.6 6.2l1.7 1.6 3.2-3.4" fill="none" stroke="#f25c5f" stroke-width="1"/></svg>Fast, simple and efficient fiscal sponsorship program</li>
      <li><svg viewBox="0 0 12 12"><circle cx="6" cy="6" r="5" fill="none" stroke="#f25c5f" stroke-width="1"/><path d="M3.6 6.2l1.7 1.6 3.2-3.4" fill="none" stroke="#f25c5f" stroke-width="1"/></svg>Free and fast approval process - our application can be completed in 30 minutes or less. There is no fee to apply, and most projects can expect to receive a response on their application within 2 weeks</li>
      <li><svg viewBox="0 0 12 12"><circle cx="6" cy="6" r="5" fill="none" stroke="#f25c5f" stroke-width="1"/><path d="M3.6 6.2l1.7 1.6 3.2-3.4" fill="none" stroke="#f25c5f" stroke-width="1"/></svg>No fees and no minimums; projects of any size are welcome to apply</li>
    </ul>
    <ul class="commit-list commit-list--right">
      <li><svg viewBox="0 0 12 12"><circle cx="6" cy="6" r="5" fill="none" stroke="#f25c5f" stroke-width="1"/><path d="M3.6 6.2l1.7 1.6 3.2-3.4" fill="none" stroke="#f25c5f" stroke-width="1"/></svg>Easy onboarding process</li>
      <li><svg viewBox="0 0 12 12"><circle cx="6" cy="6" r="5" fill="none" stroke="#f25c5f" stroke-width="1"/><path d="M3.6 6.2l1.7 1.6 3.2-3.4" fill="none" stroke="#f25c5f" stroke-width="1"/></svg>Dedicated customer service and customization of services, tailored to the individual sponsored project's needs</li>
      <li><svg viewBox="0 0 12 12"><circle cx="6" cy="6" r="5" fill="none" stroke="#f25c5f" stroke-width="1"/><path d="M3.6 6.2l1.7 1.6 3.2-3.4" fill="none" stroke="#f25c5f" stroke-width="1"/></svg>Complex, hybrid structures, partnerships and coalitions are strongly encouraged to apply</li>
    </ul>

    <div class="divider"></div>
    <h3 class="fees__heading">Fee Structure</h3>

    <section class="fee-card" style="left:46px;">
      <div class="fee-card__head">Basic<br>Fee - 4%</div>
      <div class="fee-card__body">
        <p class="fee-card__label">Limited</p>
        <ul>
          <li><svg viewBox="0 0 8 8"><circle cx="4" cy="4" r="3.4" fill="none" stroke="#777" stroke-width=".8"/><path d="M2.5 4.1l1 1 2-2.2" fill="none" stroke="#777" stroke-width=".8"/></svg>Project Fund Set-Up</li>
          <li><svg viewBox="0 0 8 8"><circle cx="4" cy="4" r="3.4" fill="none" stroke="#777" stroke-width=".8"/><path d="M2.5 4.1l1 1 2-2.2" fill="none" stroke="#777" stroke-width=".8"/></svg>Administration and Management</li>
          <li><svg viewBox="0 0 8 8"><circle cx="4" cy="4" r="3.4" fill="none" stroke="#777" stroke-width=".8"/><path d="M2.5 4.1l1 1 2-2.2" fill="none" stroke="#777" stroke-width=".8"/></svg>Financial Management</li>
          <li><svg viewBox="0 0 8 8"><circle cx="4" cy="4" r="3.4" fill="none" stroke="#777" stroke-width=".8"/><path d="M2.5 4.1l1 1 2-2.2" fill="none" stroke="#777" stroke-width=".8"/></svg>Grant Proposal Review</li>
          <li><svg viewBox="0 0 8 8"><circle cx="4" cy="4" r="3.4" fill="none" stroke="#777" stroke-width=".8"/><path d="M2.5 4.1l1 1 2-2.2" fill="none" stroke="#777" stroke-width=".8"/></svg>Grant Contract Review</li>
          <li><svg viewBox="0 0 8 8"><circle cx="4" cy="4" r="3.4" fill="none" stroke="#777" stroke-width=".8"/><path d="M2.5 4.1l1 1 2-2.2" fill="none" stroke="#777" stroke-width=".8"/></svg>Project Reporting</li>
          <li><svg viewBox="0 0 8 8"><circle cx="4" cy="4" r="3.4" fill="none" stroke="#777" stroke-width=".8"/><path d="M2.5 4.1l1 1 2-2.2" fill="none" stroke="#777" stroke-width=".8"/></svg>Insurance</li>
          <li><svg viewBox="0 0 8 8"><circle cx="4" cy="4" r="3.4" fill="none" stroke="#777" stroke-width=".8"/><path d="M2.5 4.1l1 1 2-2.2" fill="none" stroke="#777" stroke-width=".8"/></svg>Annual Audit and Form 990</li>
        </ul>
      </div>
    </section>

    <section class="fee-card" style="left:242px;">
      <div class="fee-card__head">Standard<br>Fee - 6%</div>
      <div class="fee-card__body">
        <p class="fee-card__label">Comprehensive</p>
        <p class="fee-card__sub">Basic Services +</p>
        <ul>
          <li><svg viewBox="0 0 8 8"><circle cx="4" cy="4" r="3.4" fill="none" stroke="#777" stroke-width=".8"/><path d="M2.5 4.1l1 1 2-2.2" fill="none" stroke="#777" stroke-width=".8"/></svg>Customized Financial Reporting</li>
          <li><svg viewBox="0 0 8 8"><circle cx="4" cy="4" r="3.4" fill="none" stroke="#777" stroke-width=".8"/><path d="M2.5 4.1l1 1 2-2.2" fill="none" stroke="#777" stroke-width=".8"/></svg>Monthly Financial Statements</li>
          <li><svg viewBox="0 0 8 8"><circle cx="4" cy="4" r="3.4" fill="none" stroke="#777" stroke-width=".8"/><path d="M2.5 4.1l1 1 2-2.2" fill="none" stroke="#777" stroke-width=".8"/></svg>Subgranting/regranting to U.S.based organizations</li>
          <li><svg viewBox="0 0 8 8"><circle cx="4" cy="4" r="3.4" fill="none" stroke="#777" stroke-width=".8"/><path d="M2.5 4.1l1 1 2-2.2" fill="none" stroke="#777" stroke-width=".8"/></svg>Management of Vendor and Independent Contractors (1099s)</li>
        </ul>
      </div>
    </section>

    <section class="fee-card" style="left:437px;">
      <div class="fee-card__head">Custom<br>Fee - 10%</div>
      <div class="fee-card__body">
        <p class="fee-card__label">Custom</p>
        <p class="fee-card__note">Standard Services + custom services tailored to individual project needs.</p>
        <p class="fee-card__sub">Customization Options:</p>
        <ul>
          <li><svg viewBox="0 0 8 8"><circle cx="4" cy="4" r="3.4" fill="none" stroke="#777" stroke-width=".8"/><path d="M2.5 4.1l1 1 2-2.2" fill="none" stroke="#777" stroke-width=".8"/></svg>Subgranting/regranting to international organizations</li>
          <li><svg viewBox="0 0 8 8"><circle cx="4" cy="4" r="3.4" fill="none" stroke="#777" stroke-width=".8"/><path d="M2.5 4.1l1 1 2-2.2" fill="none" stroke="#777" stroke-width=".8"/></svg>Lobbying Filings</li>
          <li><svg viewBox="0 0 8 8"><circle cx="4" cy="4" r="3.4" fill="none" stroke="#777" stroke-width=".8"/><path d="M2.5 4.1l1 1 2-2.2" fill="none" stroke="#777" stroke-width=".8"/></svg>Project Audit</li>
          <li><svg viewBox="0 0 8 8"><circle cx="4" cy="4" r="3.4" fill="none" stroke="#777" stroke-width=".8"/><path d="M2.5 4.1l1 1 2-2.2" fill="none" stroke="#777" stroke-width=".8"/></svg>Grant Writing Assistance</li>
          <li><svg viewBox="0 0 8 8"><circle cx="4" cy="4" r="3.4" fill="none" stroke="#777" stroke-width=".8"/><path d="M2.5 4.1l1 1 2-2.2" fill="none" stroke="#777" stroke-width=".8"/></svg>One-on-One Coaching</li>
        </ul>
      </div>
    </section>

    <footer class="contact">
      <span class="contact__item"><svg viewBox="0 0 24 24" aria-hidden="true"><rect x="2" y="6" width="20" height="15" rx="1.5" fill="#f25c5f"/><path d="M2.5 7 L12 14.5 L21.5 7" fill="none" stroke="#fff" stroke-width="1.6"/></svg>info@wellspringcivic.org</span>
      <span class="contact__item"><svg viewBox="0 0 24 24" aria-hidden="true"><g fill="none" stroke="#f25c5f" stroke-width="1.8"><circle cx="12" cy="12" r="9.5"/><ellipse cx="12" cy="12" rx="4.2" ry="9.5"/><path d="M2.5 12h19M4 7h16M4 17h16"/></g></svg>wellspringcivic.org</span>
    </footer>
  </article>
</body>
</html>
```